Stationery - Jewellers
Business Card, Letterhead, Envelope.
I need double sided standard sized Business Card [3.5" x 2"]
Anything that looks good. Including the fonts in logo.
Professional
Imran Kazemi
Proprietor
148 Wexcombe Lane
BX4 7QT
Leeds
United Kingdom
info@corwinthegoldcrafts.co.uk
corwinthegoldcrafts.co.uk
I will welcome any ideas.
Logo and tagline: Professionals in making your loved ones smile..
Website address.
Find us on Facebook/Twitter logos.

```html
<!DOCTYPE html>
<html lang="en">
<head>
<meta charset="utf-8">
<title>Corwin The Goldcrafts – Business Card</title>
<link href="https://fonts.googleapis.com/css2?family=Tinos:wght@400;700&family=Arimo:wght@400&display=swap" rel="stylesheet">
<style>
  :root {
    --page-bg: #e9e4dc;
    --card-black: #0b0b0b;
    --gold-light: #f6e08a;
    --gold-mid: #d9ad34;
    --gold-deep: #a8761a;
    --silver-light: #e8e8e8;
    --silver-dark: #7d7d7d;
    --ink: #1a1408;
  }
  * { margin: 0; padding: 0; box-sizing: border-box; }
  html, body {
    width: 1200px; height: 935px; overflow: hidden;
    background: var(--page-bg);
  }
  .business-card {
    position: absolute;
    left: 50px; top: 153px;
    width: 1100px; height: 629px;
    border-radius: 44px;
    overflow: hidden;
    box-shadow: 0 10px 30px rgba(0,0,0,0.25);
  }
  .card-shapes { position: absolute; inset: 0; width: 100%; height: 100%; }
  .brand {
    position: absolute;
    left: 40px; top: 80px; width: 460px;
    text-align: center;
  }
  .brand-mark {
    width: 260px; height: 260px; margin: 0 auto;
    border-radius: 50%;
    border: 6px solid var(--gold-mid);
  }
  .brand-name {
    margin-top: 50px;
    font-family: "Tinos", serif;
    font-weight: 400;
    font-size: 46px;
    line-height: 1.1;
    white-space: nowrap;
    color: var(--gold-mid);
  }
  .contact {
    position: absolute;
    right: 35px;
    text-align: right;
    color: var(--ink);
    white-space: nowrap;
  }
  .contact-name {
    top: 40px;
    font-family: "Tinos", serif;
    font-size: 30px;
    letter-spacing: 1px;
    text-transform: uppercase;
  }
  .contact-role {
    top: 80px;
    font-family: "Tinos", serif;
    font-weight: 700;
    font-size: 18px;
    text-transform: uppercase;
  }
  .contact-address, .contact-lines {
    font-family: "Arimo", sans-serif;
    font-size: 22px;
    line-height: 36px;
  }
  .contact-address { top: 400px; }
  .contact-lines { top: 492px; }
</style>
</head>
<body>
  <div class="business-card">
    <svg class="card-shapes" viewBox="0 0 1100 629" preserveAspectRatio="none" aria-hidden="true">
      <defs>
        <linearGradient id="gold-face" x1="0" y1="0" x2="1" y2="1">
          <stop offset="0" stop-color="var(--gold-light)"/>
          <stop offset="0.45" stop-color="var(--gold-mid)"/>
          <stop offset="1" stop-color="var(--gold-deep)"/>
        </linearGradient>
        <linearGradient id="silver-band" x1="0" y1="0" x2="1" y2="0">
          <stop offset="0" stop-color="var(--silver-dark)"/>
          <stop offset="0.5" stop-color="var(--silver-light)"/>
          <stop offset="1" stop-color="var(--silver-dark)"/>
        </linearGradient>
      </defs>
      <rect class="gold-panel" width="1100" height="629" fill="url(#gold-face)"/>
      <path class="silver-swoosh" d="M0,0 H775 C740,120 755,230 710,340 C665,450 610,530 580,629 H0 Z" fill="url(#silver-band)"/>
      <path class="black-panel" d="M0,0 H735 C700,120 715,230 670,330 C625,430 570,520 530,629 H0 Z" fill="var(--card-black)"/>
    </svg>

    <div class="brand">
      <div class="brand-mark"></div>
      <div class="brand-name">Corwin The Goldcrafts</div>
    </div>

    <div class="contact contact-name">Imran Kazemi</div>
    <div class="contact contact-role">Proprietor</div>
    <div class="contact contact-address">
      148 Wexcombe Lane&nbsp; BX4 7QT Leeds<br>United Kingdom
    </div>
    <div class="contact contact-lines">
      Phone : 0113 496 0731<br>
      Fax &nbsp;: 0113 496 0732<br>
      Email : info@corwinthegoldcrafts.co.uk
    </div>
  </div>
</body>
</html>
```